Verbena Home- Hang tags for Modern Handmade Home Decor products

We need to design some hang tags to use for our products, we want double tags, meaning two tags that go together on one string, two different and coordinating sizes and shapes. We have a logo, what we need is the artwork for these two tags to take to print. One tag will have the logo on one side and company information on the other, the second tag will be for product information. For example, we specialize in handmade pieces from Latin America, on the product tag I want space to write the product info but also a line for what country it's from and what community created it. I'm attaching an image of the shapes of tags that I like, along with a copy of our logo. On the larger company tag I'd like our logo in the center and a color block stripe of the yellow color of our logo at the bottom, on the flip side there will just be text, sort of our company motto. On the narrower longer product info tag I'd like a small logo at the bottom end and space for product information to be written in by hand and on the flip side of this one lines for what country it's from, what community created it and care instructions, again, all information that we will write in by hand. Please let me know if you have questions.

Target Market(s)

Design savvy, house proud, well educated people who travel and appreciate art.

Font styles to use
Sans Serif

Requirements
Must have
• I want it to look graphic, sophisticated and modern. I want to be very legible and clean.
Nice to have
• Clarity, easy to read, and maybe a bit of whimsy or lightheartedness.
Should not have
• Nothing that feels "ethnic" or "crafty:, even though our products are handmade in Latin America they are contemporary and sophisticated, not stereotypical.

```html
<!DOCTYPE html>
<html lang="en">
<head>
<meta charset="utf-8">
<title>Verbena Home — Hang Tags</title>
<link href="https://fonts.googleapis.com/css2?family=Montserrat:wght@400;500;600&display=swap" rel="stylesheet">
<style>
  :root {
    --backdrop: #f1f1f1;
    --tag-black: #111111;
    --stripe: #1c1c1c;
    --brand-yellow: #fcd116;
    --ornament-deep: #f5c400;
    --ornament-light: #fde84a;
    --type-white: #ffffff;
  }
  html, body {
    margin: 0;
    padding: 0;
    width: 1200px;
    height: 1000px;
    overflow: hidden;
    background: var(--backdrop);
  }
  .tag-set {
    position: relative;
    width: 1200px;
    height: 1000px;
  }
  .tag-set svg { display: block; }
  .tag-text { font-family: "Montserrat", sans-serif; }
  .brand-name { font-weight: 400; fill: var(--type-white); }
  .brand-url { font-weight: 600; fill: var(--brand-yellow); letter-spacing: 2.6px; }
  .origin-line { font-weight: 600; fill: var(--tag-black); letter-spacing: 4.5px; }
</style>
</head>
<body>
<main class="tag-set">
  <svg width="1200" height="1000" viewBox="0 0 1200 1000" aria-label="Verbena Home hang tags: company tag and product tag">
    <defs>
      <pattern id="fine-stripes" width="34" height="34" patternUnits="userSpaceOnUse" patternTransform="rotate(35)">
        <rect width="34" height="34" fill="var(--tag-black)"/>
        <rect width="2" height="34" fill="var(--stripe)"/>
      </pattern>
      <linearGradient id="ornament-fill" x1="0" y1="0" x2="1" y2="1">
        <stop offset="0" stop-color="var(--ornament-light)"/>
        <stop offset="1" stop-color="var(--ornament-deep)"/>
      </linearGradient>
      <clipPath id="company-tag-shape">
        <path d="M150 148 H510 Q560 148 560 200 V840 Q560 865 535 865 H107 Q82 865 82 840 V215 Z"/>
      </clipPath>
      <filter id="tag-shadow" x="-10%" y="-10%" width="120%" height="120%">
        <feDropShadow dx="3" dy="4" stdDeviation="4" flood-opacity="0.25"/>
      </filter>
    </defs>

    <!-- Company tag -->
    <g class="company-tag" filter="url(#tag-shadow)">
      <g clip-path="url(#company-tag-shape)">
        <rect x="82" y="148" width="478" height="717" fill="url(#fine-stripes)"/>
        <rect class="color-band" x="82" y="760" width="478" height="105" fill="var(--brand-yellow)"/>
      </g>
      <path class="inner-frame" d="M112 238 L178 174 H478 L530 222 V835 H112 Z" fill="none" stroke="var(--brand-yellow)" stroke-width="3"/>
      <rect class="origin-box" x="112" y="760" width="418" height="75" fill="var(--brand-yellow)" stroke="var(--tag-black)" stroke-width="3"/>
      <path class="hang-tab" d="M296 148 H360 V226 Q360 232 354 232 H302 Q296 232 296 226 Z" fill="var(--brand-yellow)"/>
      <circle class="string-hole" cx="328" cy="203" r="10" fill="var(--type-white)"/>

      <circle class="brand-dot" cx="326" cy="398" r="42" fill="var(--brand-yellow)"/>
      <text class="tag-text brand-name" x="326" y="555" font-size="66" text-anchor="middle">verbena</text>
      <text class="tag-text brand-url" x="326" y="584" font-size="14" text-anchor="middle">www.verbenahome.com</text>
      <text class="tag-text origin-line" x="318" y="807" font-size="26" text-anchor="middle">MADE IN USA</text>
    </g>

    <!-- Product tag -->
    <g class="product-tag" filter="url(#tag-shadow)">
      <path d="M852 108 H1042 L1102 186 L1118 948 H806 L786 188 Z" fill="url(#fine-stripes)"/>
      <path class="inner-frame" d="M864 120 H1032 L1088 192 L1102 934 H820 L798 192 Z" fill="none" stroke="var(--brand-yellow)" stroke-width="2"/>
      <rect class="ornament" x="826" y="152" width="222" height="530" rx="90" fill="url(#ornament-fill)" role="img" aria-label="Decorative cluster of yellow teardrop and swirl shapes"/>
      <g class="write-in-lines" stroke="var(--brand-yellow)" stroke-width="2">
        <line x1="822" y1="718" x2="1078" y2="718"/>
        <line x1="822" y1="744" x2="1079" y2="744"/>
        <line x1="822" y1="771" x2="1080" y2="771"/>
        <line x1="822" y1="797" x2="1081" y2="797"/>
        <line x1="822" y1="824" x2="1082" y2="824"/>
        <line x1="822" y1="851" x2="1083" y2="851"/>
        <line x1="822" y1="877" x2="990" y2="877"/>
      </g>
      <text class="tag-text brand-name" x="826" y="918" font-size="36">verbena</text>
      <circle class="brand-dot" cx="1056" cy="904" r="20" fill="var(--brand-yellow)"/>
    </g>
  </svg>
</main>
</body>
</html>
```